Veterinary Clinic Letterhead - Ridgeline Veterinary Surgery

We need a letterhead design for an established Veterinary Clinic in Mareeba called Ridgeline Veterinary Surgery. We are a moderate sized mixed animal veterinary clinic offering a wide variety of veterinary services. The design should use the same colour pattern as those in the logos supplied. The design should also include our address (58 Corvane Street, Tallowmere, Queensland, 4999), phone number (07 4167 5830), email (admin@ridgelinevets.example.au), website (www.ridgelinevets.example.au) and our opening hours (7:30am to 5:30pm Weekdays and 9am to 1pm Saturday).
Target Market(s)
Pet owners
Industry/Entity Type
Veterinary
Requirements
Must have
- The logo or modification of it, business address, opening hours, website, phone number and email address

```html
<!DOCTYPE html>
<html lang="en">
<head>
<meta charset="utf-8">
<title>Ridgeline Veterinary Surgery Letterhead</title>
<link href="https://fonts.googleapis.com/css2?family=Open+Sans:wght@400;600;700&display=swap" rel="stylesheet">
<style>
  :root {
    --backdrop: #333333;
    --paper: #ffffff;
    --navy: #15305f;
    --blue: #1456b0;
    --blue-light: #2f7fd6;
    --ink: #3c3f44;
    --ink-soft: #5a5e64;
    --watermark: #e6e9f0;
  }
  * { box-sizing: border-box; margin: 0; padding: 0; }
  html, body {
    width: 1200px; height: 780px; overflow: hidden;
    background: var(--backdrop);
    font-family: "Open Sans", Arial, sans-serif;
  }
  .letterhead {
    position: absolute; left: 340px; top: 22px;
    width: 520px; height: 736px;
    background: var(--paper);
    overflow: hidden;
    color: var(--ink);
  }
  .letterhead__band { position: absolute; inset: 0; }
  .watermark {
    position: absolute; left: 190px; top: 230px;
    width: 170px; height: 170px; border-radius: 50%;
    background: var(--watermark); opacity: .7;
  }
  .contact {
    position: absolute; left: 322px; top: 26px;
    font-size: 6.5px; line-height: 10px; color: var(--ink-soft);
    list-style: none;
  }
  .contact li { display: flex; align-items: center; gap: 4px; }
  .contact__icon { width: 7px; height: 7px; flex: none; }
  .contact__address { padding-left: 11px; }
  .brand {
    position: absolute; left: 42px; top: 72px;
    display: flex; align-items: center; gap: 6px;
  }
  .brand__dot { width: 20px; height: 20px; border-radius: 50%; background: var(--navy); }
  .brand__name {
    font-size: 8px; font-weight: 700; color: var(--navy);
    text-transform: uppercase; line-height: 10px; width: 92px;
  }
  .letter {
    position: absolute; left: 42px; top: 122px; width: 330px;
    font-size: 7.6px; line-height: 10.4px;
  }
  .letter__date { margin-bottom: 16px; font-size: 8px; }
  .letter__recipient { margin-bottom: 14px; font-size: 8px; line-height: 10px; }
  .letter__salutation { font-weight: 700; font-size: 8.5px; margin-bottom: 12px; }
  .letter__para { margin-bottom: 11px; }
  .signoff {
    position: absolute; right: 40px; top: 300px;
    text-align: right; font-size: 7.6px; line-height: 10px;
  }
  .signoff__name { font-size: 15px; line-height: 20px; margin: 4px 0 2px; color: var(--ink); }
  .hours {
    position: absolute; right: 24px; bottom: 18px;
    color: var(--paper); font-size: 10px;
  }
  .hours__label { font-weight: 700; }
</style>
</head>
<body>
  <main class="letterhead">
    <svg class="letterhead__band" viewBox="0 0 520 736" aria-hidden="true">
      <path d="M0,736 L0,690 C190,680 380,610 520,520 L520,736 Z" fill="var(--blue)"/>
      <path d="M0,690 C190,680 380,610 520,520" fill="none" stroke="var(--blue-light)" stroke-width="4"/>
    </svg>

    <div class="watermark" role="img" aria-label="Faint circular brand emblem behind the letter"></div>

    <ul class="contact">
      <li class="contact__address">58 Corvane Street, Tallowmere,<br>Queensland, 4999</li>
      <li>
        <svg class="contact__icon" viewBox="0 0 10 10"><circle cx="5" cy="5" r="5" fill="var(--blue)"/><path d="M3.3 2.6l1 1-0.6 0.8c0.4 0.8 1 1.4 1.8 1.8l0.8-0.6 1 1-0.8 0.9c-1.8-0.3-3.6-2.1-4-4z" fill="#fff"/></svg>
        07 4167 5830
      </li>
      <li>
        <svg class="contact__icon" viewBox="0 0 10 10"><circle cx="5" cy="5" r="5" fill="var(--blue)"/><rect x="2.5" y="3.3" width="5" height="3.4" fill="none" stroke="#fff" stroke-width=".8"/><path d="M2.5 3.3l2.5 2 2.5-2" fill="none" stroke="#fff" stroke-width=".8"/></svg>
        admin@ridgelinevets.example.au
      </li>
      <li>
        <svg class="contact__icon" viewBox="0 0 10 10"><circle cx="5" cy="5" r="5" fill="var(--blue)"/><circle cx="5" cy="5" r="2.6" fill="none" stroke="#fff" stroke-width=".7"/><path d="M2.4 5h5.2M5 2.4c-1.4 1.6-1.4 3.6 0 5.2M5 2.4c1.4 1.6 1.4 3.6 0 5.2" fill="none" stroke="#fff" stroke-width=".6"/></svg>
        www.ridgelinevets.example.au
      </li>
    </ul>

    <div class="brand">
      <span class="brand__dot"></span>
      <span class="brand__name">Ridgeline Veterinary Surgery</span>
    </div>

    <section class="letter">
      <p class="letter__date">January 12, 2021</p>
      <p class="letter__recipient">Mr. John Doe<br>President<br>AA Corporation<br>111 Street Name, Suite#<br>City, State, 12345</p>
      <p class="letter__salutation">Dear Mr. John,</p>
      <p class="letter__para">Lorem Ipsum is simply dummy text of the printing and typesetting industry. Lorem Ipsum has been the industry's standard dummy text ever since the 1500s, when an unknown printer took a galley of type and scrambled it to make a type specimen book. It has survived not only five centuries, but also the leap into electronic typesetting, remaining essentially unchanged.</p>
      <p class="letter__para">The standard chunk of Lorem Ipsum used since the 1500s is reproduced below for those interested. Sections 1.10.32 and 1.10.33 from "de Finibus Bonorum et Malorum" by Cicero are also reproduced in their exact original form, accompanied by English versions from the 1914 translation by H. Rackham.</p>
      <p class="letter__para">Lorem Ipsum is simply dummy text of the printing and typesetting industry. Lorem Ipsum has been the industry's standard dummy text ever since the 1500s, when an unknown printer took a galley of type and scrambled it to make a type specimen book. It has survived not only five centuries, but also the leap into electronic typesetting, remaining essentially unchanged. It was popularised in the</p>
    </section>

    <div class="signoff">
      <p>Sincerely Your,</p>
      <p class="signoff__name">your name</p>
      <p>Name Last Name</p>
      <p>Company Name</p>
    </div>

    <p class="hours"><span class="hours__label">Opening Hours:</span> 7:30am to 5:30pm Weekdays and 9am to 1pm Saturday</p>
  </main>
</body>
</html>
```